Mortgage Lender needs Flyers Designed

We are a wholesale mortgage lender providing mortgage services throughout the United States to mortgage brokers. We just merged with a company and need to redesign their product flyers and matrices so they are more in line with a modern and sleek look. We provide residential and commercial mortgage financing options. I have attached a document labeled FULL STACK. This is the current flyer set that needs to be redesigned for my company. There are 10 programs featured in the document. The first two pages provide a product overview and the following 17 pages are the matrices for each product. I need a design set created in either Adobe Photoshop or Adobe Indesign so we can edit the content as necessary.

Target Market(s)

Mortgage Brokers in the United States

Industry/Entity Type

Finance, Mortgage

Font styles to use
Serif
Sans Serif

Requirements
Must have
• Must include all ten programs and must be designed using Adobe Photoshop or Adobe InDesign (preferred)
Nice to have
• Great graphics and clean modern feel.
Should not have
• Typos, hard to edit fields, should not look very similar to the FULL STACK pdf attached.

```html
<!DOCTYPE html>
<html lang="en">
<head>
<meta charset="utf-8">
<title>Program Matrix Flyers</title>
<link rel="stylesheet" href="https://fonts.googleapis.com/css2?family=Libre+Baskerville:wght@700&family=Poppins:wght@400;500;600;700&display=swap">
<style>
:root{
  --stage:#b1b1b1;
  --paper:#ffffff;
  --green:#4b7030;
  --green-deep:#3c6326;
  --green-dark:#325520;
  --lime:#c9e83a;
  --mint:#e4f5d2;
  --mint-strong:#c8eaa6;
  --grey-row:#ececec;
  --ink:#1d1d1d;
  --black:#111111;
}
*{margin:0;padding:0;box-sizing:border-box}
html,body{width:1200px;height:850px;overflow:hidden;background:var(--stage)}
body{font-family:"Poppins",sans-serif;color:var(--ink);position:relative}
.flyer{position:absolute;background:var(--paper);overflow:hidden;box-shadow:0 6px 14px rgba(0,0,0,.25)}
.flyer-left{left:71px;top:92px;width:508px;height:657px}
.flyer-right{left:644px;top:96px;width:504px;height:651px}
.abs{position:absolute}
.header-photo{position:absolute;left:0;top:0;width:100%;background:linear-gradient(120deg,#557a38,#456a2c 55%,#4f7433)}
.brand{position:absolute;display:flex;align-items:center;gap:8px;color:#fff}
.brand-mark{width:26px;height:26px;border:2px solid #fff;border-radius:50%}
.brand-name{font-family:"Libre Baskerville",serif;font-size:15px;font-weight:700;line-height:1}
.brand-url{font-size:6px;letter-spacing:2px;color:#fff;position:absolute}
.title{position:absolute;text-align:right;font-family:"Libre Baskerville",serif;font-weight:700;color:#fff;font-size:26px;line-height:25px;letter-spacing:.5px}
.title-rule{position:absolute;height:2px;background:var(--black)}
.subtitle{position:absolute;text-align:right;color:var(--lime);font-size:22px;font-weight:400;letter-spacing:.5px;line-height:1}

.matrix{position:absolute;border:1.5px solid var(--black);border-radius:8px;overflow:hidden;background:#fff}
.matrix-bar{background:var(--black);color:var(--lime);font-size:7px;font-weight:500;text-align:center;height:15px;line-height:15px}
table{border-collapse:collapse;width:100%;table-layout:fixed}
.matrix table{font-size:6.5px;text-align:center}
.matrix th{background:var(--mint);font-weight:600;font-size:6px;line-height:7px;padding:3px 1px}
.matrix td{padding:0}
.matrix .fico{font-weight:600;background:#fff}
.matrix .g2 .fico{background:var(--grey-row)}
.matrix .amt{background:var(--mint)}
.matrix .rt{background:var(--mint-strong)}
.matrix .g2 td.pur,.matrix .g2 td.co{background:var(--grey-row)}
.matrix .na{background:var(--green-dark);color:#fff}
.matrix .sep td{border-top:1px solid #bbb}

.section-head{position:absolute;font-size:9px;font-weight:600;color:var(--green-deep);white-space:nowrap}
.section-head span{color:var(--ink);font-weight:400;font-size:7.5px;margin-left:6px}
.section-head.dark{color:var(--ink)}
.section-head b{font-weight:700;color:var(--green-deep)}

.fn-table{position:absolute;border-radius:6px;overflow:hidden;background:#efefef}
.fn-table table{font-size:6.5px;text-align:center}
.fn-table th{background:var(--green-deep);color:#fff;font-size:6px;font-weight:600;line-height:7px;padding:3px 1px}
.fn-table td{border-left:1px solid #fff;border-top:1px solid #d8d8d8}
.fn-table .fico{font-weight:600;line-height:8px}

.req-box{position:absolute;border:1px solid #8fb27a;border-radius:6px;border-top:none}
.req-list{position:absolute;font-size:6px;line-height:7px}
.req-row{display:flex;margin-bottom:4.5px}
.req-key{color:var(--green-deep);font-weight:600;position:relative;padding-left:7px;flex:0 0 var(--key-w)}
.req-key::before{content:"";position:absolute;left:0;top:2px;width:4px;height:4px;border-radius:50%;background:#7bbf45}
.req-key.plain::before{display:none}
.req-val{flex:1}
.bullets div{position:relative;padding-left:7px;margin-bottom:3px}
.bullets div::before{content:"";position:absolute;left:0;top:2px;width:4px;height:4px;border-radius:50%;background:var(--green-deep)}

.prop-table{position:absolute;border-radius:6px;overflow:hidden;background:#efefef}
.prop-table table{font-size:5.5px;text-align:center}
.prop-table th{background:var(--green-deep);color:#fff;font-weight:500;font-size:6.5px;height:14px}
.prop-table td{height:11px;border-top:1px solid #d6d6d6;border-left:1px solid #fff}
.prop-table td:first-child{text-align:left;padding-left:5px}

.housing{position:absolute}
.housing table{font-size:5.5px}
.housing th{color:#fff;font-size:6px;font-weight:600;line-height:7px;height:19px}
.housing td{height:13px;border-top:2px solid #fff}
.notes{position:absolute;font-size:4.5px;line-height:5.5px}
.notes div{position:relative;padding-left:6px}
.notes div::before{content:"";position:absolute;left:0;top:1.5px;width:3px;height:3px;border-radius:50%;border:1px solid #7bbf45}

.reserve-tag{position:absolute;background:var(--black);border-radius:4px;display:flex;align-items:center;justify-content:center}
.reserve-tag span{transform:rotate(-90deg);color:#fff;font-weight:700;font-size:8.5px;line-height:9px;letter-spacing:1px;text-align:center;white-space:nowrap}
.reserve-rows{position:absolute;font-size:6.5px}
.reserve-rows .row{display:flex;gap:4px;margin-bottom:3px}
.reserve-rows .k{background:#e9e9e9;font-weight:600;height:13px;line-height:13px;padding-left:7px}
.reserve-rows .v{background:#efefef;height:13px;line-height:13px;padding-left:5px;flex:1}

.panel{position:absolute;background:#fff;border-radius:8px}
.uw-list{position:absolute;font-size:6px;line-height:7px}
.uw-list .req-row{margin-bottom:9px}
.uw-divider{position:absolute;width:1px;background:#cfcfcf}

.reserve-bar{position:absolute;background:var(--black);color:var(--lime);font-size:6px;font-weight:600;text-align:center;border-radius:2px}
.reserve-table{position:absolute;font-size:6.5px}
.reserve-table .row{display:flex;gap:2px;margin-bottom:3px}
.reserve-table .k{flex:0 0 98px;background:#e6e6e6;font-weight:600;padding-left:16px;height:15px;line-height:15px}
.reserve-table .v{flex:1;background:#efefef;padding-left:10px;height:15px;line-height:15px}

.income{position:absolute;border-radius:6px;overflow:hidden;background:#efefef;font-size:6px;line-height:7px}
.income .row{display:flex;border-bottom:1px solid #d2d2d2}
.income .k{flex:0 0 68px;background:var(--green-deep);color:#fff;font-weight:600;text-align:center;padding:6px 2px}
.income .v{flex:1;padding:6px 8px}
</style>
</head>
<body>

<!-- ===== Investor Horizon flyer ===== -->
<section class="flyer flyer-left">
  <div class="header-photo" style="height:157px" role="img" aria-label="Dark green tinted photo of a business team as header backdrop"></div>

  <div class="brand" style="left:32px;top:40px">
    <div class="brand-mark"></div>
    <div class="brand-name">KEYSTONE LENDING</div>
  </div>
  <div class="brand-url" style="left:66px;top:72px">KEYSTONELEND.COM</div>

  <h1 class="title" style="right:32px;top:32px">INVESTOR<br>HORIZON</h1>
  <div class="title-rule" style="left:277px;right:32px;top:88px"></div>
  <div class="subtitle" style="right:32px;top:92px">PROGRAM MATRIX</div>

  <!-- DSCR 1.00+ -->
  <div class="matrix" style="left:32px;top:98px;width:203px;height:197px">
    <div class="matrix-bar">DSCR 1.00+ &amp; INCOME QUALIFYING</div>
    <table>
      <colgroup><col style="width:38px"><col style="width:42px"><col><col><col></colgroup>
      <tr><th>FICO</th><th>Loan Amount</th><th>Max LTV Purchase</th><th>Max LTV R/T</th><th>Max LTV Cash Out</th></tr>
      <tbody style="line-height:11.6px">
        <tr><td class="fico" rowspan="4">700</td><td class="amt">≤$1.0MM</td><td class="pur">80</td><td class="rt">80</td><td class="co">80</td></tr>
        <tr><td class="amt">$1.5MM</td><td>75</td><td class="rt">75</td><td>75</td></tr>
        <tr><td class="amt">$2.0MM</td><td>70</td><td class="rt">70</td><td>65</td></tr>
        <tr><td class="amt">$3.0MM</td><td>70</td><td class="rt">70</td><td class="na">–</td></tr>
      </tbody>
      <tbody class="g2 sep" style="line-height:11.6px">
        <tr><td class="fico" rowspan="4">699<br>–<br>660</td><td class="amt">≤$1.0MM</td><td class="pur">75</td><td class="rt">75</td><td class="co">70</td></tr>
        <tr><td class="amt">$1.5MM</td><td class="pur">75</td><td class="rt">75</td><td class="co">70</td></tr>
        <tr><td class="amt">$2.0MM</td><td class="pur">70</td><td class="rt">70</td><td class="co">60</td></tr>
        <tr><td class="amt">$3.0MM</td><td class="pur">65</td><td class="na">–</td><td class="na">–</td></tr>
      </tbody>
      <tbody style="line-height:11.6px">
        <tr><td class="fico" rowspan="4">659<br>–<br>620*</td><td class="amt">≤$1.0MM</td><td>70</td><td class="rt">70</td><td>65</td></tr>
        <tr><td class="amt">$1.5MM</td><td>65</td><td class="na">–</td><td class="na">–</td></tr>
        <tr><td class="amt">$2.0MM</td><td>65</td><td class="na">–</td><td class="na">–</td></tr>
        <tr><td class="amt">$3.0MM</td><td>60</td><td class="na">–</td><td class="na">–</td></tr>
      </tbody>
    </table>
  </div>

  <!-- DSCR 0.75 - 0.99 -->
  <div class="matrix" style="left:271px;top:133px;width:204px;height:197px">
    <div class="matrix-bar">DSCR 0.75 - 0.99</div>
    <table>
      <colgroup><col style="width:38px"><col style="width:42px"><col><col><col></colgroup>
      <tr><th>FICO</th><th>Loan Amount</th><th>Max LTV Purchase</th><th>Max LTV R/T</th><th>Max LTV Cash Out</th></tr>
      <tbody style="line-height:11.6px">
        <tr><td class="fico" rowspan="4">720</td><td class="amt">≤$1.0MM</td><td>75</td><td class="rt">75</td><td>80</td></tr>
        <tr><td class="amt">$1.5MM</td><td>70</td><td class="rt">70</td><td>75</td></tr>
        <tr><td class="amt">$2.0MM</td><td>65</td><td class="rt">65</td><td>65</td></tr>
        <tr><td class="amt">$3.0MM</td><td>65</td><td class="rt">65</td><td class="na">–</td></tr>
      </tbody>
      <tbody class="g2 sep" style="line-height:11.6px">
        <tr><td class="fico" rowspan="4">719<br>–<br>700</td><td class="amt">≤$1.0MM</td><td class="pur">70</td><td class="rt">70</td><td class="co">65</td></tr>
        <tr><td class="amt">$1.5MM</td><td class="pur">70</td><td class="rt">70</td><td class="co">65</td></tr>
        <tr><td class="amt">$2.0MM</td><td class="pur">65</td><td class="rt">60</td><td class="co">60</td></tr>
        <tr><td class="amt">$3.0MM</td><td class="pur">60</td><td class="na">–</td><td class="na">–</td></tr>
      </tbody>
      <tbody style="line-height:11.6px">
        <tr><td class="fico" rowspan="4">699<br>–<br>680</td><td class="amt">≤$1.0MM</td><td>70</td><td class="rt">70</td><td>65</td></tr>
        <tr><td class="amt">$1.5MM</td><td>70</td><td class="na">–</td><td class="na">–</td></tr>
        <tr><td class="amt">$2.0MM</td><td>65</td><td class="na">–</td><td class="na">–</td></tr>
        <tr><td class="amt">$3.0MM</td><td>60</td><td class="na">–</td><td class="na">–</td></tr>
      </tbody>
    </table>
  </div>

  <!-- Foreign National DSCR 1.00+ -->
  <div class="section-head dark" style="left:32px;top:308px">DSCR 1.00+<span>Foreign National</span></div>
  <div class="fn-table" style="left:32px;top:325px;width:214px;height:65px">
    <table>
      <colgroup><col style="width:40px"><col style="width:48px"><col><col><col></colgroup>
      <tr><th>FICO</th><th>Loan Amount</th><th>Max LTV Purchase</th><th>Max LTV R/T</th><th>Max LTV Cash Out</th></tr>
      <tr style="height:22px"><td class="fico" rowspan="2">680<br>and<br>Foreign<br>Credit</td><td>≤$1.0MM</td><td>70</td><td>65</td><td>65</td></tr>
      <tr style="height:22px"><td>$1.5MM</td><td>65</td><td>60</td><td>60</td></tr>
    </table>
  </div>

  <!-- Foreign National DSCR 0.75 -->
  <div class="section-head dark" style="left:268px;top:337px">DSCR 0.75 - 0.99<span>Foreign National</span></div>
  <div class="fn-table" style="left:263px;top:355px;width:215px;height:65px">
    <table>
      <colgroup><col style="width:40px"><col style="width:46px"><col><col><col></colgroup>
      <tr><th>FICO</th><th>Loan Amount</th><th>Max LTV Purchase</th><th>Max LTV R/T</th><th>Max LTV Cash Out</th></tr>
      <tr style="height:22px"><td class="fico" rowspan="2">680<br>and<br>Foreign<br>Credit</td><td>≤$1.0MM</td><td>70</td><td>65</td><td>65</td></tr>
      <tr style="height:22px"><td>$1.5MM</td><td>65</td><td>60</td><td>60</td></tr>
    </table>
  </div>

  <!-- General requirements -->
  <div class="section-head" style="left:30px;top:404px">General <span style="margin:0;font-weight:600;font-size:9px">Requirements</span></div>
  <div class="req-box" style="left:31px;top:414px;width:219px;height:122px"></div>
  <div class="req-list" style="left:38px;top:426px;width:208px;--key-w:62px">
    <div class="req-row"><div class="req-key">Product Type Fixed Rate</div><div class="req-val">30, 40-Yr (IO Only); 5/6 &amp; 7/6 ARM</div></div>
    <div class="req-row"><div class="req-key">Interest Only</div><div class="req-val">FICO 680+, Max 80% LTV (DSCR&lt; 1: Max 75% LTV)</div></div>
    <div class="req-row"><div class="req-key">Loan Amount</div><div class="req-val">$150k - $3.0MM</div></div>
    <div class="req-row"><div class="req-key">Loan Purpose</div><div class="req-val">Purchase, Rate/Term, Cash Out</div></div>
    <div class="req-row"><div class="req-key">Occupancy</div><div class="req-val">Non-Owner Occupied Business Purpose</div></div>
    <div class="req-row"><div class="req-key">Cash-in-Hand</div><div class="req-val">Currently free &amp; clear OR LTV&lt; 50%: Unlimited.LTV&gt;50% Max $1.0MM</div></div>
    <div class="req-row"><div class="req-key">Prepay Penalty</div><div class="req-val">As permitted by law</div></div>
  </div>

  <!-- Max LTV by property type -->
  <div class="section-head dark" style="left:29px;top:636px;display:none"></div>
  <div class="section-head dark" style="left:29px;top:545px">Max LTV by Property Type</div>
  <div class="prop-table" style="left:29px;top:563px;width:214px;height:65px">
    <table>
      <colgroup><col style="width:66px"><col><col><col></colgroup>
      <tr><th style="text-align:left;padding-left:8px">Property</th><th>Purchase</th><th>R/T</th><th>Cash Out</th></tr>
      <tr><td>Non-Warr. Condo</td><td>70</td><td>70</td><td>65</td></tr>
      <tr><td>Condo</td><td>80</td><td>80</td><td>70</td></tr>
      <tr><td>2-4 Unit DSCR &gt; 1</td><td>80</td><td>80</td><td>70</td></tr>
      <tr><td>Modular</td><td>80</td><td>80</td><td>70</td></tr>
    </table>
  </div>

  <!-- Housing information -->
  <div class="section-head" style="left:264px;top:432px">Housing <span style="margin:0;font-weight:600;font-size:9px">Information</span></div>
  <div class="housing" style="left:264px;top:451px;width:214px">
    <table>
      <colgroup><col style="width:58px"><col><col style="width:42px"></colgroup>
      <tr><th style="background:var(--green-deep)">Event Seasoning</th><th style="background:#a5d27c;color:var(--ink)">Restrictions</th><th style="background:var(--green-deep)">Mortgage DQ</th></tr>
      <tr><td style="background:#e4e4e4;font-weight:600;padding-left:6px">≥ 36 Months</td><td style="background:#fff;padding-left:4px">No adjustment at any loan amount</td><td style="padding-left:7px">1X30X12</td></tr>
      <tr><td style="background:#e4e4e4;font-weight:600;padding-left:6px">≥ 24 Months</td><td style="background:#fff;padding-left:4px">Purchase 75% Max LTV; Refi 70% Max</td><td style="padding-left:7px">2X30X12</td></tr>
      <tr><td style="background:#e4e4e4;font-weight:600;padding-left:6px">≥ 12 Months</td><td style="background:#fff;padding-left:4px">Purchase 70% Max LTV; Refi 65% Max</td><td style="padding-left:7px">0X60X12</td></tr>
    </table>
  </div>
  <div class="notes" style="left:265px;top:519px;width:215px">
    <div>Chapter 7 seasoning based on discharge date</div>
    <div>Chapter 13 seasoning based on filing date</div>
    <div>DSCR transactions require 24 months seasoning from bankruptcy or housing events</div>
    <div>Rolling mortgage lates graded as individual</div>
  </div>

  <!-- Reserves -->
  <div class="reserve-tag" style="left:264px;top:555px;width:34px;height:78px"><span>REQUIRED<br>RESERVES</span></div>
  <div class="reserve-rows" style="left:305px;top:556px;width:181px">
    <div class="row"><div class="k" style="width:67px">$150,000</div><div class="v">$500,000 3 Months</div></div>
    <div class="row"><div class="k" style="width:67px">$500,001</div><div class="v">$ $999,999 6 Months</div></div>
    <div class="row"><div class="k" style="width:67px">$1.0MM</div><div class="v">$1.49MM 9 Months</div></div>
    <div class="row"><div class="k" style="width:67px">$1.5MM</div><div class="v">12 Months</div></div>
    <div class="row"><div class="k" style="width:67px">Interest Only</div><div class="v">6 Months Minimum</div></div>
  </div>
</section>

<!-- ===== Cobalt Horizon flyer ===== -->
<section class="flyer flyer-right">
  <div class="header-photo" style="height:183px" role="img" aria-label="Dark green tinted photo of a business team as header backdrop"></div>

  <div class="brand" style="left:36px;top:40px">
    <div class="brand-mark"></div>
    <div class="brand-name">KEYSTONE LENDING</div>
  </div>
  <div class="brand-url" style="left:70px;top:72px">KEYSTONELEND.COM</div>

  <h1 class="title" style="right:31px;top:32px">COBALT<br>HORIZON</h1>
  <div class="title-rule" style="left:276px;right:31px;top:88px"></div>
  <div class="subtitle" style="right:31px;top:92px">PROGRAM MATRIX</div>

  <div class="matrix" style="left:31px;top:107px;width:204px;height:251px">
    <div class="matrix-bar" style="height:17px;line-height:17px;font-size:7.5px">FULL OR ALTERNATIVE DOCUMENT</div>
    <table>
      <colgroup><col style="width:38px"><col style="width:45px"><col><col><col></colgroup>
      <tr><th>FICO</th><th>Loan Amount</th><th>Max LTV Purchase</th><th>Max LTV R/T</th><th>Max LTV Cash Out</th></tr>
      <tbody style="line-height:24.5px">
        <tr><td class="fico" rowspan="4">720</td><td class="amt">≤$1.0MM</td><td>80</td><td class="rt">80</td><td>80</td></tr>
        <tr><td class="amt">$1.5MM</td><td>75</td><td class="rt">75</td><td>75</td></tr>
        <tr><td class="amt">$2.0MM</td><td>70</td><td class="rt">70</td><td>70</td></tr>
        <tr><td class="amt">$2.5MM</td><td>70</td><td class="rt">70</td><td>70</td></tr>
      </tbody>
      <tbody class="g2 sep" style="line-height:24.5px">
        <tr><td class="fico" rowspan="4" style="line-height:8px">719<br>–<br>700</td><td class="amt">≤$1.0MM</td><td class="pur">75</td><td class="rt">75</td><td class="co">75</td></tr>
        <tr><td class="amt">$1.5MM</td><td class="pur">75</td><td class="rt">75</td><td class="co">75</td></tr>
        <tr><td class="amt">$2.0MM</td><td class="pur">70</td><td class="rt">70</td><td class="co">70</td></tr>
        <tr><td class="amt">$3.0MM</td><td class="pur">65</td><td class="rt">65</td><td class="co">65</td></tr>
      </tbody>
    </table>
  </div>

  <!-- Underwriting -->
  <div class="panel" style="left:250px;top:127px;width:223px;height:140px"></div>
  <div class="section-head dark" style="left:262px;top:137px"><b>Underwriting</b> Requirements</div>
  <div class="uw-divider" style="left:322px;top:156px;height:80px"></div>
  <div class="uw-list" style="left:259px;top:157px;width:210px;--key-w:66px">
    <div class="req-row"><div class="req-key">Gift Funds</div><div class="req-val">Minimum contribution: 5% primary</div></div>
    <div class="req-row"><div class="req-key">Document Age</div><div class="req-val">Income, assets, title documents: 90 days Credit Report, Appraisal: 120 days</div></div>
    <div class="req-row"><div class="req-key">Assets</div><div class="req-val">Minimum of 30-days asset verification required; any large deposit must be sourced</div></div>
    <div class="req-row"><div class="req-key">DTI Requirements</div><div class="req-val">Standard 50% back end; see guidelines for restrictions to allow for 55%</div></div>
  </div>

  <div class="reserve-bar" style="left:256px;top:267px;width:213px;height:11px;line-height:11px">Required Reserves</div>
  <div class="reserve-table" style="left:256px;top:283px;width:212px">
    <div class="row"><div class="k">LTV ≤ 80%</div><div class="v">3 Months PITIA (ITIA-IO)</div></div>
    <div class="row"><div class="k">LTV &gt; 80%</div><div class="v">6 Months PITIA (ITIA-IO)</div></div>
    <div class="row"><div class="k">Loan &gt; $1.5MM</div><div class="v">9 Months PITIA (ITIA-IO)</div></div>
    <div class="row"><div class="k">Loan &gt; $2.0MM</div><div class="v">12 Months PITIA (ITIA-IO)</div></div>
  </div>

  <!-- Income -->
  <div class="section-head dark" style="left:262px;top:363px"><b>Income</b> Requirements</div>
  <div class="income" style="left:262px;top:378px;width:211px;height:107px">
    <div class="row"><div class="k">Full Document</div><div class="v">12 or 24 month full documentation income</div></div>
    <div class="row" style="height:61px"><div class="k">Alt-Document</div><div class="v">Self-employed borrowers only:<br>&nbsp;&nbsp;12 or 24 months business or personal bank statements<br>&nbsp;&nbsp;CPA prepared P&amp;L + 2 months bank statements(limited to 80% CLTV)<br>&nbsp;&nbsp;1099 only</div></div>
    <div class="row" style="border:none"><div class="k" style="padding:4px 2px">Asset Depletion</div><div class="v" style="padding:4px 8px">Max 80% LTV. See guidelines for details.</div></div>
  </div>

  <!-- General requirements -->
  <div class="section-head" style="left:32px;top:375px">General <span style="margin:0;font-weight:600;font-size:9px">Requirements</span></div>
  <div class="req-box" style="left:32px;top:382px;width:216px;height:231px"></div>
  <div class="req-list" style="left:37px;top:394px;width:206px;--key-w:67px">
    <div class="req-row"><div class="req-key plain">Exceptions</div><div class="req-val">Exceptions</div></div>
    <div class="req-row"><div class="req-key">Product Type</div><div class="req-val">Fixed Rate: 15, 30, 40-Years (IO Only)</div></div>
    <div class="req-row"><div class="req-key">Interest Only</div><div class="req-val">Eligible</div></div>
    <div class="req-row"><div class="req-key">Loan Amount</div><div class="req-val">$350k - $2.5MM</div></div>
    <div class="req-row"><div class="req-key">Loan Purpose</div><div class="req-val">Purchase, Rate/Term, Cash Out</div></div>
    <div class="req-row"><div class="req-key">Occupancy</div><div class="req-val">Owner Occupied (primary and 2nd homes)</div></div>
    <div class="req-row"><div class="req-key">Cash-in-Hand</div><div class="req-val">Max unlimited</div></div>
    <div class="req-row"><div class="req-key">Property Type</div><div class="req-val bullets">
      <div>Single Family</div><div>2-unit</div><div>Condo (max 75% CLTV)</div>
      <div>Non-warrantable Condo (max CLTV:Purchase 75%; Refi 65%)</div><div>Rural case by case</div></div></div>
    <div class="req-row"><div class="req-key">Second Home</div><div class="req-val">$1.5MM max loan amount</div></div>
    <div class="req-row"><div class="req-key">Servicing</div><div class="req-val">Impounds required; no option to waive</div></div>
    <div class="req-row"><div class="req-key">Acreage</div><div class="req-val">Up to 20 acres, non-rural. Acreage ≥ 10, max 80% CLTV</div></div>
  </div>

  <!-- Housing -->
  <div class="section-head" style="left:263px;top:498px">Housing <span style="margin:0;font-weight:600;font-size:9px">Information</span></div>
  <div class="req-box" style="left:263px;top:504px;width:210px;height:107px"></div>
  <div class="req-list" style="left:268px;top:517px;width:200px;--key-w:68px">
    <div class="req-row" style="border-bottom:1px solid #d6d6d6;padding-bottom:6px;margin-bottom:6px"><div class="req-key">History</div><div class="req-val">1x30x12 Max; requires 5% LTV reduction</div></div>
    <div class="req-row" style="border-bottom:1px solid #d6d6d6;padding-bottom:6px;margin-bottom:6px"><div class="req-key">Event Seasoning</div><div class="req-val">BK/FC/SS/DIL/Mod ≥ 36 Months</div></div>
    <div class="req-row"><div class="req-key">Appraisals</div><div class="req-val">FNMA form 1004, 1025, 1073 with interior/ exterior inspection. Appraisal review product required unless 2nd appraisal obtained 2nd appraisal required for loans &gt; $2.0MM</div></div>
  </div>
</section>

</body>
</html>
```